Need a website where people can find information about the newly formed Prairie Valuation Review Board. Soon after, we will need a place to publish our findings as we audit each municipality in the State of Wisconsin. I have a logo (designed by Sketch Hive), a MS Word document showing the content and a set of images to choose from that we can purchase from PhotoVault.com (found here https://www.photovaultimages.example/shared/folders/-Tr8mQpLzNwXAvbYe-Kd)

```html
<!DOCTYPE html>
<html lang="en">
<head>
<meta charset="utf-8">
<title>Prairie Valuation Review Board</title>
<link href="https://fonts.googleapis.com/css2?family=Poppins:ital,wght@0,400;0,500;0,600;1,500&display=swap" rel="stylesheet">
<style>
:root{
  --green:#3b8a17;
  --dark:#2c2c2c;
  --charcoal:#3d3d3d;
  --ink:#222;
  --text:#333;
  --white:#fff;
  --rule:#8a8a8a;
}
*{box-sizing:border-box;margin:0;padding:0}
html,body{width:1200px;height:4142px;overflow:hidden}
body{font-family:'Poppins',sans-serif;color:var(--text);background:var(--white);position:relative}
.abs{position:absolute}
a{color:inherit;text-decoration:none}

/* top bar */
.topbar{left:0;top:0;width:1200px;height:43px;background:var(--dark)}
.topbar nav{position:absolute;right:174px;top:12px;display:flex;gap:11px;font-size:13.5px;font-weight:500;color:var(--white)}

/* hero */
.hero{left:0;top:43px;width:1200px;height:802px;overflow:hidden}
.hero-photo{position:absolute;inset:0;background:linear-gradient(180deg,#2f7fd6 0%,#5aa1e6 35%,#c9d3dc 55%,#e9ecee 68%,#6f8a4c 82%,#3b4a2e 100%)}
.brand{position:absolute;left:172px;top:48px;display:flex;align-items:center;gap:12px}
.brand-mark{width:38px;height:38px;background:var(--green)}
.brand-name{font-size:17px;font-weight:600;color:var(--white);line-height:1.15;width:180px}
.phone{position:absolute;left:758px;top:26px;display:flex;align-items:center;gap:8px;color:var(--white);font-size:16px;font-weight:500}
.phone-icon{width:30px;height:30px;border-radius:50%;background:var(--white);display:flex;align-items:center;justify-content:center}
.donate{position:absolute;left:931px;top:18px;width:95px;height:42px;border-radius:21px;background:var(--white);color:var(--ink);font-size:15px;font-weight:500;display:flex;align-items:center;justify-content:center}
.hero-nav{position:absolute;right:174px;top:79px;display:flex;gap:14px;color:var(--white);font-size:14px;font-weight:500}
.title-band{position:absolute;left:200px;top:251px;width:800px;height:70px;background:linear-gradient(90deg,rgba(20,50,110,0) 0%,rgba(20,50,110,.55) 20%,rgba(20,50,110,.55) 80%,rgba(20,50,110,0) 100%);display:flex;align-items:center;justify-content:center}
.title-band h1{font-size:28px;font-weight:600;color:var(--white);letter-spacing:.2px}
.tagline{position:absolute;left:0;width:1200px;top:737px;text-align:center;font-style:italic;font-weight:500;font-size:27px;color:var(--white)}

/* shared */
.btn{display:inline-flex;align-items:center;justify-content:center;background:var(--green);color:var(--white);font-weight:500;border-radius:26px}
.h2{font-size:30px;font-weight:600;color:var(--ink)}
.body-copy{font-size:12.5px;line-height:22.5px;color:var(--ink);text-align:justify}
.body-copy p+p{margin-top:8px}

/* who we are */
.who-mark{left:172px;top:941px;width:290px;height:306px;display:flex;flex-direction:column;align-items:center;justify-content:center;gap:18px}
.who-mark .sq{width:120px;height:120px;background:var(--green)}
.who-mark span{font-size:26px;font-weight:600;color:var(--green);text-align:center;line-height:1.2}
.who{left:532px;top:928px;width:496px}
.who .h2{margin-bottom:12px}
.who .btn{margin-top:26px;width:121px;height:48px;font-size:15px}

/* uniform */
.uniform{left:0;top:1351px;width:1200px;height:600px;background:linear-gradient(90deg,#fbfbfc 0%,#f1f3f6 55%,#e4e8ee 100%)}
.uniform-photo{position:absolute;left:690px;top:0;width:510px;height:600px;background:linear-gradient(160deg,#e9ecef 0%,#c9b5a6 40%,#9a8a7a 60%,#c6d2c0 85%,#e4e8ee 100%)}
.uniform-copy{position:absolute;left:172px;top:103px;width:496px}
.uniform-copy .h2{margin-bottom:12px}
.uniform-copy .btn{margin-top:28px;width:121px;height:48px;font-size:15px}

/* cards */
.recs-title{left:0;width:1200px;top:2036px;text-align:center}
.card{top:2180px;width:221px;height:273px;background:var(--white);box-shadow:0 2px 10px rgba(0,0,0,.16);text-align:center;padding-top:70px}
.card .icon{position:absolute;left:50%;top:-40px;margin-left:-45px;width:90px;height:90px;border-radius:50%;background:var(--charcoal);display:flex;align-items:center;justify-content:center}
.card.is-green .icon,.card.is-green .btn{background:var(--green)}
.card h3{font-size:17px;font-weight:600;color:var(--ink);margin-bottom:10px}
.card p{font-size:11.5px;line-height:19px;color:var(--ink);padding:0 12px}
.card .btn{margin-top:22px;width:95px;height:35px;font-size:11.5px;background:var(--charcoal)}

/* recommendations detail */
.dept{left:0;top:2554px;width:1200px;height:546px;background:linear-gradient(90deg,#f5f5f5 0%,#e6e6e6 45%,#dadada 100%)}
.dept-photo{position:absolute;left:0;top:0;width:500px;height:546px;background:linear-gradient(135deg,#f2f2f2 0%,#c9c9c9 45%,#8f8f8f 60%,#d8d8d8 100%)}
.dept-copy{position:absolute;left:555px;top:96px;width:473px}
.dept-copy .lead{font-size:15px;color:var(--ink);margin:10px 0 14px}
.dept-copy ul{list-style:none;font-size:12px;line-height:22.5px;color:var(--ink)}
.dept-copy .btn{margin-top:24px;width:119px;height:48px;font-size:15px}

/* contact */
.contact-title{left:0;width:1200px;top:3181px;text-align:center}
.field{border:1.5px solid #7a7a7a;border-radius:26px;font-size:13.5px;color:var(--ink);padding:13px 18px}
.send{left:529px;top:3521px;width:142px;height:48px;font-size:15px}

/* footer */
.footer{left:0;top:3655px;width:1200px;height:487px;background:var(--dark);color:var(--white)}
.foot-brand{position:absolute;left:172px;top:85px;width:230px;height:246px;display:flex;flex-direction:column;align-items:center;justify-content:center;gap:16px}
.foot-brand .sq{width:96px;height:96px;background:var(--green)}
.foot-brand span{font-size:22px;font-weight:600;text-align:center;line-height:1.2}
.foot-links{position:absolute;left:503px;top:89px}
.foot-links h4{font-size:19px;font-weight:600;margin-bottom:12px}
.cols{display:flex;gap:0}
.cols ul{list-style:none;font-size:13.5px;line-height:30px;width:288px}
.foot-rule{position:absolute;left:172px;top:399px;width:854px;height:1px;background:var(--rule)}
.copyright{position:absolute;left:0;width:1200px;top:431px;text-align:center;font-size:13.5px;font-weight:500}
</style>
</head>
<body>

<header class="abs topbar">
  <nav><a>Blog</a><a>Audits</a><a>PVRB Recommendations</a><a>Meet the Volunteers</a><a>Corrections</a><a>Contact Us</a></nav>
</header>

<section class="abs hero">
  <div class="hero-photo" role="img" aria-label="State capitol building with white dome under a blue sky, trees in front"></div>
  <div class="brand"><div class="brand-mark"></div><div class="brand-name">Prairie Valuation Review Board</div></div>
  <div class="phone">
    <span class="phone-icon"><svg width="15" height="15" viewBox="0 0 24 24"><path d="M6.6 10.8a15.1 15.1 0 0 0 6.6 6.6l2.2-2.2c.3-.3.7-.4 1-.2 1.1.4 2.3.6 3.6.6.6 0 1 .4 1 1V20c0 .6-.4 1-1 1C10.6 21 3 13.4 3 4c0-.6.4-1 1-1h3.5c.6 0 1 .4 1 1 0 1.3.2 2.5.6 3.6.1.3 0 .7-.2 1z" fill="#2c2c2c"/></svg></span>
    + 1 608 555 0142
  </div>
  <a class="donate">Donate</a>
  <nav class="hero-nav"><a>Who We Are</a><a>Wisconsin's Non-Uniform Property Tax Problem</a><a>What is Uniform Taxation?</a></nav>
  <div class="title-band"><h1>PRAIRIE VALUATION REVIEW BOARD</h1></div>
  <p class="tagline">Working to ensure uniform property taxation statewide</p>
</section>

<div class="abs who-mark"><div class="sq"></div><span>Prairie Valuation<br>Review Board</span></div>
<section class="abs who">
  <h2 class="h2">WHO WE ARE</h2>
  <div class="body-copy">
    <p>The Prairie Valuation Review Board (PVRB) is a non-partisan, not-for-profit, watchdog organization with a mission to ensure uniform property taxation statewide. It was started in February of 2022 as the Prairie Valuation Review Board, LLC and does business as the Prairie Valuation Review Board.</p>
    <p>The Prairie Valuation Review Board audits local municipal governments who are responsible for producing a uniform property tax assessment roll each year. The audit looks for evidence that property tax assessments are uniform as well as evidence that they are not uniform.</p>
  </div>
  <a class="btn">Read More</a>
</section>

<section class="abs uniform">
  <div class="uniform-photo" role="img" aria-label="Model house resting on banknotes and a tax form"></div>
  <div class="uniform-copy">
    <h2 class="h2">WHAT IS UNIFORM TAXATION?</h2>
    <div class="body-copy">
      <p>Uniform taxation means similar properties have similar values for taxation purposes.</p>
      <p style="margin-top:0">For example, if you own a condominium assessed for tax purposes at $200,000 and your neighbor has the same unit but is assessed at $160,000, your values, and therefore your taxes, will be significantly different. You will be paying more of the tax burden than your neighbor, even though the market value of both units is the same. This is non-uniform taxation.</p>
      <p>Two properties are often not identical; but to the extent that they are the same their assessed values should be the same. To the extent they are different their assessed values should be different.</p>
    </div>
    <a class="btn">Read More</a>
  </div>
</section>

<h2 class="abs h2 recs-title">PVRB RECOMMENDATIONS</h2>

<article class="abs card is-green" style="left:129px">
  <div class="icon"><svg width="48" height="48" viewBox="0 0 48 48" fill="none" stroke="#fff" stroke-width="2.2"><path d="M6 18 24 8l18 10H6z"/><path d="M10 22v16M18 22v16M30 22v16M38 22v16M5 40h38M24 3v5"/><path d="M24 3h6v3h-6"/></svg></div>
  <h3>For Municipalities</h3>
  <p>The Prairie Valuation Review Board audits local municipal governments who are responsible.</p>
  <a class="btn">Read More</a>
</article>
<article class="abs card" style="left:370px">
  <div class="icon"><svg width="48" height="48" viewBox="0 0 48 48" fill="none" stroke="#fff" stroke-width="2.2"><path d="M34 22V7H10v34h14"/><path d="M15 14h14M15 20h14M15 26h8"/><circle cx="33" cy="33" r="6"/><path d="m37.5 37.5 5 5"/></svg></div>
  <h3>For Boards of Review</h3>
  <p>The Prairie Valuation Review Board audits local municipal governments who are responsible.</p>
  <a class="btn">Read More</a>
</article>
<article class="abs card" style="left:610px">
  <div class="icon"><svg width="48" height="48" viewBox="0 0 48 48" fill="none" stroke="#fff" stroke-width="2.2"><path d="M6 16 24 6l18 10H6zM8 20h32M12 23v14M20 23v14M28 23v14M36 23v14M6 40h36"/></svg></div>
  <h3>For Legislators</h3>
  <p>The Prairie Valuation Review Board audits local municipal governments who are responsible.</p>
  <a class="btn">Read More</a>
</article>
<article class="abs card" style="left:849px">
  <div class="icon"><svg width="48" height="48" viewBox="0 0 48 48" fill="none" stroke="#fff" stroke-width="2.2"><path d="M24 6v34M14 40h20M8 12h32"/><path d="m12 12-6 14h12zM36 12l-6 14h12z"/></svg></div>
  <h3>For Taxpayers</h3>
  <p>The Prairie Valuation Review Board audits local municipal governments who are responsible.</p>
  <a class="btn">Read More</a>
</article>

<section class="abs dept">
  <div class="dept-photo" role="img" aria-label="Finger pressing down one pan of a metal balance scale"></div>
  <div class="dept-copy">
    <h2 class="h2">PVRB RECOMMENDATIONS</h2>
    <p class="lead">The Department of Revenue needs to do the following:</p>
    <ul>
      <li>Hire enough qualified people with real assessment experience to comply with WI Stat 73.03.</li>
      <li>Develop a pass/fail system to measure uniformity.</li>
      <li>Use that system to determine which municipal property tax rolls pass and which ones fail.</li>
      <li>Hold municipalities accountable if their property tax rolls are not uniform.</li>
      <li>Strategically audit municipalities and assessment firms to ensure they are not avoiding accountability by gaming the system.</li>
    </ul>
    <a class="btn">Read More</a>
  </div>
</section>

<h2 class="abs h2 contact-title">CONTACT FORM</h2>
<div class="abs field" style="left:172px;top:3261px;width:278px;height:48px">First Name</div>
<div class="abs field" style="left:462px;top:3261px;width:276px;height:48px">Last Name</div>
<div class="abs field" style="left:750px;top:3261px;width:276px;height:48px">Email Address</div>
<div class="abs field" style="left:172px;top:3328px;width:854px;height:48px">Subject</div>
<div class="abs field" style="left:172px;top:3396px;width:854px;height:98px;border-radius:30px">Message</div>
<a class="abs btn send">Send Message</a>

<footer class="abs footer">
  <div class="foot-brand"><div class="sq"></div><span>Prairie Valuation<br>Review Board</span></div>
  <div class="foot-links">
    <h4>QUICK LINKS</h4>
    <div class="cols">
      <ul><li>Home</li><li>Blog</li><li>Audits</li><li>PVRB Recommendations</li><li>Meet the Volunteers</li><li>Corrections</li><li>Contact Us</li></ul>
      <ul><li>Who We Are</li><li>Wisconsin's Non-Uniform Property</li><li>Tax Problem</li><li>Taxation?</li><li>What is Uniform</li></ul>
    </div>
  </div>
  <div class="foot-rule"></div>
  <p class="copyright">Copyrights @ 2022 PVRB. All Rights Reserved.</p>
</footer>

</body>
</html>
```